Brightpath Desk letterhead and envelope

Design a formal (8.5x11) letterhead and envelope for sales outreach and legal matters. Using design input from https://www.brightpathdesk.com/ and the attached documents.

Industry/Entity Type

Software Service

Requirements
Must have
• These 4 hex colors are our official colors:
• #355c98 [blue]
• #1eb1a2 [teal]
• #fdba12 [gold]
• #f1653b [orange]
• So no other colors besides these should be used.

```html
<!DOCTYPE html>
<html lang="en">
<head>
<meta charset="utf-8">
<title>Brightpath Desk Letterhead</title>
<link href="https://fonts.googleapis.com/css2?family=Didact+Gothic&family=Arimo:wght@400;700&display=swap" rel="stylesheet">
<style>
  :root {
    --brand-blue: #355c98;
    --brand-teal: #1eb1a2;
    --brand-gold: #fdba12;
    --brand-orange: #f1653b;
    --paper: #ffffff;
    --ink: #3a3a3a;
    --backdrop: #dde5f2;
  }
  * { box-sizing: border-box; margin: 0; padding: 0; }
  html, body { width: 1200px; height: 893px; overflow: hidden; background: var(--backdrop); }
  .canvas { position: relative; width: 1200px; height: 893px; }
  .letterhead {
    position: absolute; left: 275px; top: 25px; width: 650px; height: 843px;
    background: var(--paper); box-shadow: 0 10px 40px rgba(53,92,152,.18);
    font-family: "Didact Gothic", sans-serif; color: var(--ink);
  }
  .brand {
    position: absolute; left: 70px; top: 48px; display: flex; align-items: center; gap: 14px;
  }
  .brand-dot {
    width: 46px; height: 46px; border-radius: 50%; border: 4px solid var(--brand-blue);
  }
  .brand-name {
    font-family: "Didact Gothic", sans-serif; font-size: 40px; color: var(--brand-blue); letter-spacing: .5px;
  }
  .header-band {
    position: absolute; left: 70px; right: 0; top: 112px; height: 20px; background: var(--brand-blue);
    color: #fff; font-family: "Arimo", sans-serif; font-weight: 700; font-size: 12px;
    letter-spacing: 1.5px; display: flex; align-items: center; justify-content: center;
  }
  .header-address {
    position: absolute; left: 70px; right: 0; top: 138px; text-align: center;
    font-family: "Arimo", sans-serif; font-size: 12px; color: var(--brand-blue);
  }
  .letter-body {
    position: absolute; left: 70px; right: 70px; top: 215px;
    font-size: 12.5px; line-height: 19px;
  }
  .letter-body p { margin-bottom: 19px; }
  .signature { position: absolute; right: 50px; top: 650px; text-align: left; }
  .signature-name { font-size: 15px; }
  .signature-title { font-size: 10.5px; margin-top: 4px; }
  .signature-rule { position: absolute; right: 0; top: 695px; width: 180px; height: 10px; background: var(--brand-blue); }
  .contact-row {
    position: absolute; left: 70px; right: 30px; top: 730px; display: flex; justify-content: center; gap: 26px;
    font-family: "Arimo", sans-serif; font-size: 12px; color: var(--brand-blue);
  }
  .contact-item { display: flex; align-items: center; gap: 6px; }
  .contact-item svg { width: 14px; height: 14px; }
  .footer-band { position: absolute; left: 70px; right: 40px; top: 760px; height: 22px; background: var(--brand-blue); }
</style>
</head>
<body>
<div class="canvas">
  <article class="letterhead">
    <header>
      <div class="brand">
        <span class="brand-dot"></span>
        <span class="brand-name">brightpath desk</span>
      </div>
      <div class="header-band">www.brightpathdesk.com</div>
      <div class="header-address">240 Harlow Street, Suite 4C, Marston, GA 30090</div>
    </header>

    <section class="letter-body">
      <p>Lorem ipsum dolor sit amet, consectetur adipiscing elit. Donec orci purus, luctus vitae dignissim eu, iaculis sed purus. Vivamus faucibus, ipsum nec aliquet viverra, leo mauris condimentum ligula, sit amet sagittis enim ligula quis arcu. Nam egestas tortor id nisi porttitor mattis. In tortor ante, ultricies in suscipit a, tempus non massa. Vivamus et auctor mi. Fusce vel massa nulla. Phasellus nec eros mauris, et scelerisque orci. Donec malesuada orci vitae nulla accumsan porta a id massa.</p>
      <p>Quisque accumsan iaculis magna sit amet fringilla. Maecenas consequat, magna eget tincidunt semper, odio nibh rutrum mi, id feugiat ante nisi eu risus. Vestibulum nunc orci, rhoncus a placerat in, ultricies in mi. Cras mattis varius eros, vel fringilla nisi suscipit eget. Quisque scelerisque sagittis nulla at porttitor. Mauris a justo et tellus interdum tristique. Sed id augue vitae urna euismod commodo aliquet a quam. Pellentesque arcu velit, cursus et malesuada ut, consequat et diam. Nullam erat sem, rhoncus id ullamcorper vitae, rhoncus et arcu. In ultricies ultricies nulla.</p>
      <p>Kut rutrum nisi iaculis at. Donec eu magna a metus ornare faucibus. Fusce aliquet faucibus ultricies. Morbi semper, est id tincidunt gravida, sem arcu adipiscing lacus, ac bibendum nulla leo eu purus. Quisque nec diam sed risus consectetur a accumsan quis quis nibh. Vestibulum id purus lorem. Donec eu magna a metus ornare faucibus. Fusce aliquet faucibus ultricies. Morbi semper, est id tincidunt gravida, sem arcu adipiscing lacus, ac bibendum nulla leo eu purus. Quisque nec diam sed risus consectetur a accumsan quis quis nibh. Vestibulum id purus lorem.</p>
    </section>

    <div class="signature">
      <div class="signature-name">Owen Caldwell</div>
      <div class="signature-title">Co-Founder &amp; CEO</div>
    </div>
    <div class="signature-rule"></div>

    <footer>
      <div class="contact-row">
        <span class="contact-item">
          <svg viewBox="0 0 14 14"><circle cx="7" cy="7" r="7" fill="var(--brand-blue)"/><rect x="4.5" y="3" width="5" height="8" rx="1" fill="#fff"/></svg>555 210-4400
        </span>
        <span class="contact-item">
          <svg viewBox="0 0 14 14"><circle cx="7" cy="7" r="7" fill="var(--brand-blue)"/><path d="M3.5 6 Q7 3 10.5 6 L9.5 7 L8.5 6.2 L5.5 6.2 L4.5 7 Z M4.5 8 H9.5 V10 H4.5 Z" fill="#fff"/></svg>555 310 2299
        </span>
        <span class="contact-item">
          <svg viewBox="0 0 14 14"><circle cx="7" cy="7" r="7" fill="var(--brand-blue)"/><rect x="3.5" y="4.5" width="7" height="5" fill="#fff"/><path d="M3.5 4.5 L7 7.3 L10.5 4.5" stroke="var(--brand-blue)" stroke-width="1" fill="none"/></svg>hello@brightpathdesk.com
        </span>
      </div>
      <div class="footer-band"></div>
    </footer>
  </article>
</div>
</body>
</html>
```